New Podcast focussing on non-mainstream interventions for guidance needs podcast art

I need an exquisite piece of podcast art work for the launch of my new podcast 'Past the Hollow'. This podcast explores unorthodox, esoteric and unconventional methods to find peace, clarity and direction in life. Topics include family Constellations Systems, Psychedelics, Equine Therapy and Floatation to name a few. A teaser has been posted on Brevlo with a strong response. The audience is primarily midlifers or those in a career/personal crisis of direction. It's meant to comfort, inform and empower and offer other ways rather than mainstream to work out what to do with your life. The file shared with you shows the pic used on Brevlo as it's illustrating the idea of illumination. You can use it or not, and whilst I am ex-Military, I don't want the cover to convey an overly military influence. I'd like 'Past the Hollow' to feature on the art work and my name, Margot Pennick. I'd like inspiration, creativity, and the idea of hope conveyed as well as clarity and courage. Whilst the podcast is about finding your direction please do no use compass images or cross road images as that is too obvious.
Hope that all helps. Looking forward to your ideas.

```html
<!DOCTYPE html>
<html lang="en">
<head>
<meta charset="utf-8">
<title>Past the Hollow — Podcast Cover</title>
<link href="https://fonts.googleapis.com/css2?family=Bebas+Neue&family=Yellowtail&display=swap" rel="stylesheet">
<style>
  :root {
    --ink: #ffffff;
    --night: #1c0d0b;
    --ember: #4a2520;
    --dusk: #6e3a38;
    --glow: #fff4ec;
    --haze: #b77a78;
    --field: #5a3622;
  }
  html, body {
    margin: 0;
    padding: 0;
    width: 1200px;
    height: 1200px;
    overflow: hidden;
    background: var(--night);
  }
  .cover {
    position: relative;
    width: 1200px;
    height: 1200px;
    overflow: hidden;
    font-family: "Bebas Neue", "Arial Narrow", sans-serif;
    color: var(--ink);
  }
  .cover__scene {
    position: absolute;
    inset: 0;
    background:
      radial-gradient(circle at 1006px 312px, var(--glow) 0, rgba(255,236,225,0.9) 28px, rgba(230,160,160,0.45) 70px, rgba(160,90,100,0.15) 180px, rgba(0,0,0,0) 320px),
      radial-gradient(ellipse 520px 160px at 900px 620px, rgba(183,122,120,0.35), rgba(0,0,0,0) 100%),
      linear-gradient(180deg, rgba(0,0,0,0) 0, rgba(0,0,0,0) 70%, var(--field) 84%, var(--night) 100%),
      linear-gradient(90deg, var(--night) 0%, var(--ember) 35%, var(--dusk) 70%, var(--ember) 100%);
  }
  .cover__title {
    position: absolute;
    left: 130px;
    top: 150px;
    margin: 0;
    font-weight: 400;
    line-height: 0.8;
    text-transform: uppercase;
  }
  .cover__title span {
    display: block;
    letter-spacing: 0;
  }
  .cover__title .line-1 { font-size: 320px; }
  .cover__title .line-2 { font-size: 320px; margin-top: 8px; }
  .cover__title .line-3 { font-size: 292px; margin-top: 8px; }
  .host {
    position: absolute;
    left: 124px;
    top: 1020px;
    width: 474px;
    height: 130px;
  }
  .host__frame {
    position: absolute;
    inset: 0;
  }
  .host__with {
    position: absolute;
    left: 58px;
    top: -30px;
    font-family: "Yellowtail", cursive;
    font-size: 46px;
    line-height: 1;
    margin: 0;
  }
  .host__name {
    position: absolute;
    left: 0;
    right: 0;
    top: 46px;
    margin: 0;
    text-align: center;
    font-size: 64px;
    line-height: 1;
    letter-spacing: 4px;
  }
</style>
</head>
<body>
  <main class="cover">
    <div class="cover__scene" role="img" aria-label="Night photograph: a kneeling figure in silhouette between dark trees watches a bright flare of light drift through a hazy dusky-red sky"></div>

    <h1 class="cover__title">
      <span class="line-1">Past</span>
      <span class="line-2">The</span>
      <span class="line-3">Hollow</span>
    </h1>

    <div class="host">
      <svg class="host__frame" width="474" height="130" viewBox="0 0 474 130" aria-hidden="true">
        <path d="M52 0.5 H0.5 V129.5 H473.5 V0.5 H206" fill="none" stroke="#ffffff" stroke-width="1.2"/>
      </svg>
      <span class="host__with">With</span>
      <p class="host__name">Margot Pennick</p>
    </div>
  </main>
</body>
</html>
```